Reputable business cards for Diplom Kauffrau, Privat und Geschäftslich

The business cards should be reputable, valuable and elegant in order to be able to use them for business. The design should also include a sophistication that is conspicuous. This could be a picture, an ornament, a sublime print or a kind of logo of the initials of my name "MD". The font should be clear and legible.
Target Market(s)
Business contacts, friends and acquaintances
Contact Information for Business Card
Diplom-Kauffrau Mirela Donat
Lindenhofweg 7 50931 Kerpen
Mobil +49 171 804 29 57
e-mail mirela.donat@postwerk.de
Colors
Designer to choose colors to be used in the design.
Requirements
Must have
- Clear and easy to read font My name in larger font than the other information Visual conspicuity / specificity
Nice to have
- Different colors
Should not have
- Ornate font, playful

```html
<!DOCTYPE html>
<html lang="de">
<head>
<meta charset="utf-8">
<title>Visitenkarte Mirela Donat</title>
<link href="https://fonts.googleapis.com/css2?family=Josefin+Sans:wght@300;400;600&display=swap" rel="stylesheet">
<style>
  :root {
    --backdrop: #d9d9d9;
    --card: #2f3032;
    --card-edge: #242527;
    --monogram: #3a3b3e;
    --accent: #4f8fd0;
    --text-light: #e4e6ea;
  }
  * { margin: 0; padding: 0; box-sizing: border-box; }
  html, body {
    width: 1200px;
    height: 1200px;
    overflow: hidden;
  }
  body {
    background: radial-gradient(circle at 50% 45%, #ececec 0%, var(--backdrop) 75%);
    font-family: "Josefin Sans", sans-serif;
    position: relative;
  }
  .business-card {
    position: absolute;
    left: 100px;
    top: 277px;
    width: 1000px;
    height: 647px;
    background: linear-gradient(160deg, #353638 0%, var(--card) 55%, var(--card-edge) 100%);
  }
  .monogram {
    position: absolute;
    left: 430px;
    top: 110px;
    width: 200px;
    height: 200px;
    display: flex;
    align-items: center;
    justify-content: center;
    gap: 14px;
  }
  .monogram-ring {
    width: 22px;
    height: 22px;
    border-radius: 50%;
    background: var(--monogram);
  }
  .monogram-name {
    font-weight: 600;
    font-size: 96px;
    line-height: 1;
    color: var(--monogram);
    letter-spacing: 0.02em;
  }
  .contact-block {
    position: absolute;
    left: 228px;
    top: 425px;
  }
  .holder-name {
    font-weight: 400;
    font-size: 40px;
    color: var(--accent);
    letter-spacing: 0.01em;
    margin-bottom: 12px;
  }
  .contact-line {
    display: flex;
    align-items: center;
    gap: 30px;
    font-weight: 300;
    font-size: 25px;
    color: var(--text-light);
    margin-bottom: 10px;
  }
  .contact-item {
    display: flex;
    align-items: center;
    gap: 6px;
  }
  .contact-icon { width: 24px; height: 24px; }
  .address {
    font-weight: 300;
    font-size: 25px;
    color: var(--text-light);
    letter-spacing: 0.16em;
  }
</style>
</head>
<body>
  <article class="business-card">
    <div class="monogram">
      <span class="monogram-ring"></span>
      <span class="monogram-name">MD</span>
    </div>
    <div class="contact-block">
      <h1 class="holder-name">Diplom-Kauffrau Mirela Donat</h1>
      <p class="contact-line">
        <span class="contact-item">
          <svg class="contact-icon" viewBox="0 0 24 24" aria-hidden="true">
            <rect x="6" y="2" width="12" height="20" rx="2" fill="none" stroke="#4f8fd0" stroke-width="1.8"/>
            <line x1="10" y1="18.5" x2="14" y2="18.5" stroke="#4f8fd0" stroke-width="1.5"/>
          </svg>
          +49 171 804 29 57
        </span>
        <span class="contact-item">
          <svg class="contact-icon" viewBox="0 0 24 24" aria-hidden="true">
            <rect x="2" y="5" width="20" height="14" fill="none" stroke="#4f8fd0" stroke-width="1.8"/>
            <polyline points="2,5 12,13 22,5" fill="none" stroke="#4f8fd0" stroke-width="1.8"/>
          </svg>
          mirela.donat@postwerk.de
        </span>
      </p>
      <p class="address">Lindenhofweg 7 | 50931 Kerpen</p>
    </div>
  </article>
</body>
</html>
```